Lena's Yuletide Album CD Art for Album Release Dec 14, 2017.

CD cover for Lena Hartwell's "Lena's Yuletide" Christmas music album. Must include hi-res photo and LH logo front and back, "Lena Hartwell", and "Lena's Yuletide". Also, please add "Vol 1" somewhere in the work and on the spine. Lena plans multiple albums of Christmas music in the coming years. CD design format templates attached to design to for production. If possible, consider some blank space on the CD and cover, so Lena can autograph same, when sold in person. Include the song listing and times of each song as seen on the attached word doc. Order pf artwork: 1) Front CD Cover with feature photo and album title; 2) Inside left with a few pics of Lena in the studio; 3) Back of CD case listing songs, contributors etc. Song listing info to follow, since we are in the studio now. Expecting 11 songs. I have uploaded the list to be placed on the back of the CD. I will have the times to fill in by then end of next week, since Lena is recording again on Tuesday Nov 21.
Updates

Need to add the UPC code to the lower back of the cd. UPC-A code is: 403186529074. Use this UPC label maker: https://www.tagprintbox.example/label-generator-tools/Barcode-Generator.aspx

Update #1 a) Please use script font for the album cover text. b) Remove the words "Lena Hartwell" off of the LH logo used on the front cover. c) Do not use photos from other album covers in the project. They are copyright protected by Tallow Records. They were provided as examples. d) You can get a flavor of LEna's work on the landing page of her website: www.lenahartwell.example, and the upcoming Christmas concert Thks, Dennis

Target Market(s)

Lena Hartwell fan base, and all Christmas music lovers.

Font styles to use
Script

Colors

Designer to choose colors to be used in the design.

Requirements
Must have
• Lena Hartwell's "Lena's Yuletide" Christmas music album. Must include hi-res photo and LH logo front and back, "Lena Hartwell", and "Lena's Yuletide". Also, please add "Vol 1" somewhere in the work and on the spine.
• A little Christmas art flare added.
Nice to have
• If possible, consider some blank space on the CD and cover, so Lena can autograph same, when sold in person.

```html
<!DOCTYPE html>
<html lang="en">
<head>
<meta charset="utf-8">
<title>Lena's Yuletide – Vol 1</title>
<link href="https://fonts.googleapis.com/css2?family=Great+Vibes&family=Cinzel:wght@400;600&display=swap" rel="stylesheet">
<style>
  :root {
    --backdrop: #f7e2a8;
    --ink: #0b0906;
    --gold: #d9b25a;
    --gold-soft: #8a6a2c;
    --ivory: #f4ecdc;
    --silver-light: #e9e6df;
    --silver-dark: #9c978c;
  }
  * { margin: 0; padding: 0; box-sizing: border-box; }
  html, body { width: 1200px; height: 789px; overflow: hidden; }
  body {
    background: var(--backdrop);
    font-family: "Cinzel", serif;
    position: relative;
  }

  /* Disc label */
  .disc {
    position: absolute;
    left: 70px; top: 135px;
    width: 520px; height: 520px;
    border-radius: 50%;
    background: var(--ink);
    overflow: hidden;
    border: 4px solid #2a241a;
  }
  .disc-sparkle-tree {
    position: absolute;
    left: 190px; top: 330px;
    width: 200px; height: 180px;
    background: radial-gradient(ellipse at 50% 55%, rgba(217,178,90,0.75) 0%, rgba(138,106,44,0.35) 45%, rgba(11,9,6,0) 72%);
  }
  .disc-brand {
    position: absolute; left: 0; right: 0; top: 34px;
    display: flex; align-items: center; justify-content: center; gap: 6px;
    color: var(--gold); font-size: 11px; letter-spacing: 2px;
  }
  .brand-dot { width: 16px; height: 16px; border-radius: 50%; background: var(--gold); }
  .disc-title {
    position: absolute; left: 0; right: 0; top: 62px;
    text-align: center;
    font-family: "Great Vibes", cursive;
    color: var(--ivory); font-size: 46px;
    transform: rotate(-8deg);
  }
  .track-list {
    position: absolute;
    list-style: none;
    color: var(--ivory);
    font-size: 10.5px; letter-spacing: 0.6px;
    line-height: 27px;
  }
  .track-list--left { left: 36px; top: 178px; }
  .track-list--right { left: 340px; top: 150px; }
  .disc-hub {
    position: absolute; left: 185px; top: 185px;
    width: 150px; height: 150px; border-radius: 50%;
    background: radial-gradient(circle, var(--silver-light) 0%, var(--silver-dark) 100%);
    border: 3px solid #6e6a60;
  }
  .disc-hub::after {
    content: ""; position: absolute; left: 50%; top: 50%;
    width: 40px; height: 40px; margin: -20px 0 0 -20px;
    border-radius: 50%; background: var(--backdrop);
    border: 3px solid var(--silver-dark);
  }

  /* Front cover */
  .cover {
    position: absolute;
    left: 620px; top: 115px;
    width: 540px; height: 540px;
    background: var(--ink);
    overflow: hidden;
  }
  .cover-sparkles {
    position: absolute; inset: 0;
    background:
      radial-gradient(ellipse at 30% 20%, rgba(217,178,90,0.55) 0%, rgba(11,9,6,0) 55%),
      radial-gradient(ellipse at 80% 10%, rgba(217,178,90,0.3) 0%, rgba(11,9,6,0) 45%);
  }
  .cover-photo {
    position: absolute; left: 40px; top: 70px;
    width: 290px; height: 470px;
    background: linear-gradient(160deg, #3a2a18 0%, #6b4b2a 45%, #b58f4e 100%);
    border-radius: 140px 140px 0 0;
    opacity: 0.85;
  }
  .cover-brand {
    position: absolute; left: 300px; top: 150px; width: 200px;
    display: flex; flex-direction: column; align-items: center; gap: 6px;
    color: var(--gold);
  }
  .cover-brand-mark { display: flex; align-items: center; gap: 6px; font-size: 12px; letter-spacing: 2px; }
  .cover-brand-mark .brand-dot { width: 22px; height: 22px; }
  .cover-artist { font-size: 17px; letter-spacing: 2px; }
  .cover-title {
    position: absolute; left: 330px; top: 250px;
    font-family: "Great Vibes", cursive;
    color: var(--ivory); font-size: 62px; line-height: 0.95;
    transform: rotate(-14deg);
  }
  .cover-volume {
    display: block; text-align: right;
    font-size: 22px; color: var(--gold);
  }
</style>
</head>
<body>
  <section class="disc" aria-label="Disc label">
    <div class="disc-sparkle-tree" role="img" aria-label="Golden sparkle Christmas tree"></div>
    <div class="disc-brand"><span class="brand-dot"></span>LH</div>
    <h2 class="disc-title">Lena's Yuletide</h2>
    <ol class="track-list track-list--left">
      <li>O Holy Night</li>
      <li>Hark The Herald Angels</li>
      <li>Silent Night</li>
      <li>Joy To The World</li>
      <li>O Come All Ye Faithful</li>
      <li>First Noel</li>
    </ol>
    <ol class="track-list track-list--right">
      <li>Have A Merry Little Christmas</li>
      <li>Winter Wonderland</li>
      <li>Go Tell It On The Mountain</li>
      <li>Christmas Time Is Here</li>
      <li>A Medley For The Season</li>
    </ol>
    <div class="disc-hub"></div>
  </section>

  <section class="cover" aria-label="Front cover">
    <div class="cover-sparkles" role="img" aria-label="Gold sparkle and bokeh lights on black"></div>
    <div class="cover-photo" role="img" aria-label="Feature photo of Lena Hartwell in a gold gown"></div>
    <div class="cover-brand">
      <div class="cover-brand-mark"><span class="brand-dot"></span>LH</div>
      <div class="cover-artist">LENA HARTWELL</div>
    </div>
    <h1 class="cover-title">Lena's<br>Yuletide<span class="cover-volume">Vol 1</span></h1>
  </section>
</body>
</html>
```